Exercise Physiologist needs a Brochure

I am Exercise Physiologist providing exercise therapy for a variety of conditions. I have a logo and recent business card design. I like the black background like the front of the business cards. I have attached the flyer information required. I have also attached a few photos however they do not have to be used, happy to have no photos at all.

Industry/Entity Type

Health And Wellness

Font styles to use
Sans Serif

Requirements
Must have
• Please also add instagram @varnolhealth
Nice to have
• tri-fold brochure

```html
<!DOCTYPE html>
<html lang="en">
<head>
<meta charset="utf-8">
<title>Varnol – Tri-fold Brochure</title>
<link rel="stylesheet" href="https://fonts.googleapis.com/css2?family=Open+Sans:wght@300;400;600&display=swap">
<style>
  :root {
    --ink: #1d1d1f;
    --ink-soft: #2a2a2d;
    --paper: #ffffff;
    --paper-shade: #eef0f2;
    --blue: #3a86c8;
    --blue-light: #5fa9e2;
    --grey: #9aa0a6;
    --text-dark: #3b3b3b;
    --text-light: #e8e8e8;
    --stage: #e4e4e4;
  }
  * { box-sizing: border-box; margin: 0; padding: 0; }
  html, body {
    width: 1200px; height: 2400px; overflow: hidden;
    background: var(--stage);
    font-family: "Open Sans", Arial, sans-serif;
  }
  .canvas { position: relative; width: 1200px; height: 2400px; }
  .sheet {
    position: absolute; left: 30px; width: 1140px; height: 808px;
    display: flex; box-shadow: 0 10px 30px rgba(0,0,0,.18);
  }
  .sheet--outside { top: 260px; }
  .sheet--inside { top: 1330px; }
  .panel {
    position: relative; width: 380px; height: 808px; overflow: hidden;
  }
  .panel + .panel { border-left: 1px solid rgba(0,0,0,.08); }
  .panel--dark { background: var(--ink); color: var(--text-light); }
  .panel--light { background: var(--paper); color: var(--text-dark); }
  .layer { position: absolute; left: 0; top: 0; width: 380px; height: 808px; }
  .content { position: absolute; left: 0; right: 0; }

  .headline {
    color: var(--blue); font-weight: 300; font-size: 34px; line-height: 1.1;
    text-transform: uppercase; letter-spacing: .5px;
  }
  .subhead { font-weight: 600; font-size: 13px; line-height: 1.35; }
  .section-title { color: var(--blue-light); font-weight: 400; font-size: 19px; line-height: 1.25; }
  .body-copy { font-size: 12.5px; line-height: 1.6; }
  .body-copy + .body-copy { margin-top: 12px; }
  .rule { width: 150px; height: 2px; background: var(--blue); margin: 14px auto; }

  .brand { display: flex; align-items: center; gap: 10px; }
  .brand__dot {
    width: 34px; height: 34px; border-radius: 50%; background: var(--blue);
  }
  .brand__name { color: var(--blue); font-size: 34px; font-weight: 400; line-height: 1; }

  .person-name { color: var(--blue-light); font-weight: 300; font-size: 38px; line-height: 1.05; }
  .person-role { font-weight: 300; font-size: 22px; color: var(--paper); }
  .person-quals { font-size: 12px; line-height: 1.6; color: var(--text-light); }

  .contact-line { display: flex; align-items: center; gap: 10px; font-size: 13px; }
  .social { display: flex; gap: 22px; font-size: 12px; color: var(--text-light); }
  .social span { display: flex; align-items: center; gap: 7px; }
  .social i { width: 16px; height: 16px; border-radius: 50%; border: 1.5px solid var(--grey); display: inline-block; }

  .condition-list { list-style: none; font-size: 13px; line-height: 1.7; }
  .condition-list li { display: flex; gap: 10px; }
  .condition-list b {
    flex: none; width: 16px; height: 16px; margin-top: 3px; border-radius: 50%;
    background: var(--blue); color: var(--paper); font-size: 9px; font-weight: 600;
    display: flex; align-items: center; justify-content: center;
  }
</style>
</head>
<body>
<main class="canvas">

  <!-- Outside of the tri-fold -->
  <section class="sheet sheet--outside">

    <!-- Inner flap -->
    <article class="panel panel--light">
      <svg class="layer" viewBox="0 0 380 808" aria-hidden="true">
        <path d="M0 630 Q190 560 380 610 V808 H0Z" fill="var(--ink)"/>
        <path d="M0 618 Q190 548 380 598" fill="none" stroke="var(--blue)" stroke-width="7"/>
        <circle cx="120" cy="580" r="78" fill="var(--paper-shade)" stroke="#cfd3d7" stroke-width="6"/>
      </svg>
      <svg class="layer" viewBox="0 0 380 808" role="img" aria-label="Close-up photo of running shoes on a track">
        <defs><radialGradient id="shoes" cx="50%" cy="45%" r="60%"><stop offset="0" stop-color="#b7a58c"/><stop offset="1" stop-color="#4e4a44"/></radialGradient></defs>
        <circle cx="120" cy="580" r="72" fill="url(#shoes)"/>
      </svg>
      <div class="content" style="top:48px; padding:0 34px;">
        <h2 class="headline">Heal<br>through<br>movement</h2>
        <p class="subhead" style="margin-top:14px; color:var(--text-dark); font-style:normal;">Discover how important the correct exercise technique is to your success</p>
        <p class="body-copy" style="margin-top:12px;">Performing the right exercise the wrong way can do more harm than good. I can teach you what, how and when to perform your tailored exercise program to get the best results.</p>
      </div>
      <div class="content" style="top:690px; padding:0 34px; color:var(--paper);">
        <p style="font-size:17px; font-weight:300; line-height:1.35;">Call or email me today to see how I can help you.</p>
        <div class="contact-line" style="margin-top:12px;">
          <svg width="20" height="20" viewBox="0 0 20 20" aria-hidden="true"><circle cx="10" cy="10" r="9" fill="none" stroke="var(--blue-light)" stroke-width="1.5"/><path d="M7 5.5l1.6 2.2-1 1.1a7 7 0 0 0 3.6 3.6l1.1-1 2.2 1.6-.8 1.6c-4 0-8-4-8-8z" fill="var(--blue-light)"/></svg>
          <span>0400 000 123</span>
        </div>
      </div>
    </article>

    <!-- Back panel -->
    <article class="panel panel--dark">
      <svg class="layer" viewBox="0 0 380 808" aria-hidden="true">
        <path d="M0 0 H380 V40 Q200 150 0 60Z" fill="var(--paper)"/>
        <path d="M0 74 Q200 166 380 52" fill="none" stroke="var(--blue)" stroke-width="5"/>
        <path d="M0 560 Q190 520 380 570" fill="none" stroke="#333" stroke-width="2"/>
      </svg>
      <div class="content" style="top:130px; text-align:center;">
        <div class="brand" style="justify-content:center;">
          <span class="brand__dot" style="width:72px; height:72px; border:5px solid var(--paper);"></span>
        </div>
        <h1 class="person-name" style="margin-top:26px;">Clara Dunmore</h1>
        <p class="person-role">Exercise Physiologist</p>
        <div class="rule"></div>
        <p class="body-copy">Unit 4, 12 Harlow St EASTBROOK<br>(Kestrel Fitness)</p>
        <p class="body-copy" style="margin-top:6px;">hello@varnolhealth.example</p>
      </div>
      <div class="content" style="top:630px; padding:0 40px;">
        <div class="brand" style="justify-content:center;">
          <span class="brand__dot"></span><span class="brand__name">varnol</span>
        </div>
        <div class="social" style="justify-content:center; margin-top:34px;">
          <span><i></i>varnol</span>
          <span><i></i>@varnolhealth</span>
        </div>
      </div>
    </article>

    <!-- Front cover -->
    <article class="panel panel--dark">
      <svg class="layer" viewBox="0 0 380 808" aria-hidden="true">
        <path d="M0 0 H380 V140 Q200 130 0 190Z" fill="var(--paper)"/>
        <path d="M0 196 Q200 136 380 146" fill="none" stroke="#7d848b" stroke-width="8"/>
      </svg>
      <svg class="layer" viewBox="0 0 380 808" role="img" aria-label="Photo of a woman running along a tree-lined path">
        <defs><linearGradient id="run" x1="0" y1="0" x2="0" y2="1"><stop offset="0" stop-color="#a9b06a"/><stop offset=".55" stop-color="#5f7a3c"/><stop offset="1" stop-color="#8e8a80"/></linearGradient></defs>
        <path d="M0 202 Q200 142 380 152 V560 Q200 610 0 530Z" fill="url(#run)"/>
      </svg>
      <svg class="layer" viewBox="0 0 380 808" aria-hidden="true">
        <path d="M0 540 Q200 622 380 568" fill="none" stroke="var(--blue)" stroke-width="7"/>
      </svg>
      <div class="content" style="top:46px; padding:0 34px;">
        <div class="brand" style="justify-content:flex-end;"><span class="brand__dot"></span><span class="brand__name">varnol</span></div>
      </div>
      <div class="content" style="top:640px; padding:0 34px; text-align:right;">
        <h1 class="person-name">Clara Dunmore</h1>
        <p class="person-role">Exercise Physiologist</p>
        <p class="person-quals" style="margin-top:10px;">B.AppSci – Human Movt<br>Grad Dip – Ex Rehab<br>Cert IV – Training &amp; Assessment</p>
      </div>
    </article>
  </section>

  <!-- Inside of the tri-fold -->
  <section class="sheet sheet--inside">

    <article class="panel panel--dark">
      <svg class="layer" viewBox="0 0 380 808" role="img" aria-label="Photo of a knee held in both hands with a red area of pain">
        <defs><linearGradient id="knee" x1="0" y1="0" x2="1" y2="1"><stop offset="0" stop-color="#cfcfcf"/><stop offset=".5" stop-color="#c98a86"/><stop offset="1" stop-color="#6b6b6b"/></linearGradient></defs>
        <path d="M0 600 Q190 560 380 610 V808 H0Z" fill="url(#knee)"/>
      </svg>
      <svg class="layer" viewBox="0 0 380 808" aria-hidden="true">
        <path d="M0 596 Q190 554 380 604" fill="none" stroke="var(--blue)" stroke-width="6"/>
      </svg>
      <div class="content" style="top:44px; padding:0 34px;">
        <h2 class="headline">Heal<br>through<br>movement</h2>
        <p class="subhead" style="margin-top:12px; color:var(--paper);">Don't let the right exercise but the wrong technique hinder your recovery</p>
        <h3 class="section-title" style="margin-top:24px;">What is an Exercise Physiologist?</h3>
        <p class="body-copy" style="margin-top:10px;">Exercise Physiologists are university educated health professionals trained to provide exercise therapy for pain and injury, pre and post surgery, mental health and chronic disease. They are registered providers with RoadCover, WorkShield, PublicCare and Veterans Health Office and many Private Health funds.</p>
      </div>
    </article>

    <article class="panel panel--light">
      <div class="content" style="top:50px; padding:0 40px; text-align:center;">
        <div class="brand" style="justify-content:center;">
          <span class="brand__dot" style="width:64px; height:64px;"></span>
        </div>
        <h3 class="section-title" style="margin-top:40px; color:var(--blue);">How can I help you?</h3>
        <div class="rule"></div>
      </div>
      <div class="content" style="top:250px; padding:0 40px;">
        <p class="body-copy">I have over 13 years of experience working as an Exercise Physiologist and have been working in the sport and fitness industry since 1995. I understand that everyone's health and exercise experience is unique and will tailor a program to suit you and your lifestyle.</p>
        <p class="body-copy">Managing your condition involves working with you to develop the best exercises and teaching you the correct techniques essential to improve. Home and gym based programs can be provided.</p>
        <p class="body-copy">When appropriate I can also work with your current treating health practitioner to provide a holistic approach to your recovery.</p>
      </div>
    </article>

    <article class="panel panel--dark">
      <svg class="layer" viewBox="0 0 380 808" role="img" aria-label="Photo of a rack of dumbbells in a gym">
        <defs><linearGradient id="gym" x1="0" y1="0" x2="1" y2="1"><stop offset="0" stop-color="#c6d3dc"/><stop offset=".6" stop-color="#5d6a73"/><stop offset="1" stop-color="#2c3136"/></linearGradient></defs>
        <path d="M0 0 H380 V170 Q200 220 0 290Z" fill="url(#gym)"/>
      </svg>
      <svg class="layer" viewBox="0 0 380 808" aria-hidden="true">
        <path d="M0 296 Q200 224 380 176" fill="none" stroke="var(--blue)" stroke-width="6"/>
      </svg>
      <div class="content" style="top:300px; padding:0 34px;">
        <h3 class="section-title">Common conditions that benefit from exercise therapy</h3>
        <ol class="condition-list" style="margin-top:14px;">
          <li><b>1</b>Back pain</li>
          <li><b>2</b>Joint pain</li>
          <li><b>3</b>Arthritis</li>
          <li><b>4</b>Pain relating to exercise</li>
          <li><b>5</b>Anxiety relating to exercise</li>
          <li><b>6</b>Depression and Anxiety</li>
          <li><b>7</b>Chronic diseases such as diabetes, heart and lung disease</li>
          <li><b>8</b>Motor vehicle accidents</li>
        </ol>
        <p class="body-copy" style="margin-top:22px;">Performing the right exercise the wrong way can do more harm than good. I can teach you what, how and when to perform your tailored exercise program to get the best results.</p>
      </div>
    </article>
  </section>

</main>
</body>
</html>
```